The Brightwater Compass Business Card

We need an attractive business card with the logo that we bought from ArtVantly last year.
Our mission is to contribute to change the way today's leaders manage business companies bringing value to the workplace and helping them to build a new model of creating wealth.
Our logo is clear about our values : we seek Positive Change through People and are convinced that the pursuit of individual well-being and the chase of economic results can converge with the right management.
Management Consulting
Corinne Fabrelle
+34 612 98 70 31
corinne.fabrelle@thebrightwatercompass-mail.net
www.thebrightwatercompass-mail.net

```html
<!DOCTYPE html>
<html lang="en">
<head>
<meta charset="utf-8">
<title>The Brightwater Compass – Business Card</title>
<link rel="stylesheet" href="https://fonts.googleapis.com/css2?family=Cinzel:wght@600&family=EB+Garamond:wght@400;600&display=swap">
<style>
  :root {
    --teal: #0e7f7c;
    --paper: #fbfbfb;
    --ink: #4a4a4a;
    --backdrop: #ececec;
    --white: #ffffff;
  }
  * { box-sizing: border-box; margin: 0; padding: 0; }
  html, body { width: 1200px; height: 586px; overflow: hidden; }
  body {
    background: var(--backdrop);
    position: relative;
    font-family: "EB Garamond", Georgia, serif;
  }
  .card {
    position: absolute;
    top: 129px;
    width: 502px;
    height: 301px;
  }
  .card--front { left: 61px; background: var(--teal); }
  .card--back { left: 619px; background: var(--paper); }

  .brand-name {
    font-family: "Cinzel", "Times New Roman", serif;
    font-weight: 600;
    white-space: nowrap;
    position: absolute;
    left: 0; right: 0;
    text-align: center;
  }
  .card--front .brand-name {
    color: var(--white);
    font-size: 27px;
    top: 160px;
  }
  .card--back .brand-name {
    color: var(--teal);
    font-size: 21px;
    top: 42px;
  }

  .contact-name {
    position: absolute;
    left: 27px; top: 174px;
    font-size: 19px;
    font-weight: 600;
    color: var(--teal);
  }
  .contact-role {
    position: absolute;
    left: 27px; top: 198px;
    font-size: 11px;
    color: var(--ink);
  }
  .role-rule {
    position: absolute;
    left: 68px; top: 204px;
    width: 404px; height: 2px;
    background: var(--teal);
  }
  .contact-list {
    position: absolute;
    left: 27px; top: 229px;
    list-style: none;
  }
  .contact-list li {
    display: flex;
    align-items: center;
    height: 24px;
    font-size: 13px;
    color: var(--ink);
  }
  .contact-icon { width: 18px; height: 18px; margin-right: 7px; flex: none; }
</style>
</head>
<body>
  <section class="card card--front" aria-label="Card front">
    <p class="brand-name">The Brightwater Compass</p>
  </section>

  <section class="card card--back" aria-label="Card back">
    <p class="brand-name">The Brightwater Compass</p>
    <h1 class="contact-name">Corinne Fabrelle</h1>
    <p class="contact-role">Founder</p>
    <div class="role-rule"></div>
    <ul class="contact-list">
      <li>
        <svg class="contact-icon" viewBox="0 0 18 18" aria-hidden="true">
          <circle cx="9" cy="9" r="9" fill="var(--teal)"/>
          <path d="M4.5 8 Q9 4.5 13.5 8 L12.3 9.2 L10.6 8.2 L10.6 7.3 Q9 6.8 7.4 7.3 L7.4 8.2 L5.7 9.2 Z" fill="#fff"/>
          <rect x="6" y="9.6" width="6" height="3.2" rx="0.6" fill="#fff"/>
        </svg>
        +34 612 98 70 31
      </li>
      <li>
        <svg class="contact-icon" viewBox="0 0 18 18" aria-hidden="true">
          <circle cx="9" cy="9" r="9" fill="var(--teal)"/>
          <rect x="4.5" y="5.8" width="9" height="6.4" fill="#fff"/>
          <path d="M4.5 5.8 L9 9.6 L13.5 5.8" fill="none" stroke="var(--teal)" stroke-width="0.9"/>
        </svg>
        corinne.fabrelle@thebrightwatercompass-mail.net
      </li>
    </ul>
  </section>
</body>
</html>
```